Business Card Design Project

Velvet Harbor is a Boutique Clothing. On the business cards I would like to have this included
Website: www.velvetharbor-example.com
Email: shop@velvetharbor-example.com
Owner: Mai Torres & Bo Rinaldi

Industry/Entity Type

Business

Contact Information for Business Card

I wanted something simple and elegant. I have attach business logo.

```html
<!DOCTYPE html>
<html lang="en">
<head>
<meta charset="utf-8">
<title>Velvet Harbor – Business Card</title>
<link rel="stylesheet" href="https://fonts.googleapis.com/css2?family=Tinos:ital@1&family=Questrial&display=swap">
<style>
  :root {
    --backdrop: #e7e4df;
    --card-charcoal: #343334;
    --card-black: #161616;
    --card-white: #ffffff;
    --ink-light: #ffffff;
    --ink-dark: #1c1c1c;
    --brand-ink: #2e2e2e;
  }
  html, body {
    margin: 0;
    width: 1200px;
    height: 902px;
    overflow: hidden;
    background: var(--backdrop);
  }
  .canvas {
    position: relative;
    width: 1200px;
    height: 902px;
  }
  .business-card {
    position: absolute;
    left: 100px;
    top: 166px;
    width: 1000px;
    height: 570px;
    border-radius: 28px;
    overflow: hidden;
    background: var(--card-charcoal);
    box-shadow: 0 10px 30px rgba(0,0,0,0.18);
  }
  .card-waves {
    position: absolute;
    inset: 0;
  }
  .wave-band { fill: var(--card-black); }
  .wave-field { fill: var(--card-white); }

  .owners {
    position: absolute;
    right: 59px;
    top: 52px;
    text-align: right;
    color: var(--ink-light);
  }
  .owners-names {
    font-family: "Tinos", "Times New Roman", serif;
    font-style: italic;
    font-size: 35px;
    line-height: 1;
    letter-spacing: 0.3px;
  }
  .owners-role {
    font-family: "Questrial", "Century Gothic", sans-serif;
    font-size: 21px;
    line-height: 1;
    margin-top: 4px;
  }

  .brand {
    position: absolute;
    left: 205px;
    top: 291px;
    transform: translate(-50%, -50%);
    display: flex;
    align-items: center;
    gap: 12px;
    color: var(--brand-ink);
    font-family: "Questrial", "Century Gothic", sans-serif;
    font-size: 34px;
    white-space: nowrap;
  }
  .brand-dot {
    width: 12px;
    height: 12px;
    border-radius: 50%;
    background: var(--brand-ink);
  }

  .contact-list {
    position: absolute;
    left: 566px;
    top: 360px;
    margin: 0;
    padding: 0;
    list-style: none;
    color: var(--ink-dark);
    font-family: "Questrial", "Century Gothic", sans-serif;
    font-size: 23.5px;
  }
  .contact-item {
    display: flex;
    align-items: center;
    gap: 8px;
    height: 40px;
  }
  .contact-icon {
    width: 30px;
    height: 30px;
    flex: none;
  }
</style>
</head>
<body>
<main class="canvas">
  <section class="business-card" aria-label="Velvet Harbor business card">
    <svg class="card-waves" viewBox="0 0 1000 570" width="1000" height="570" aria-hidden="true">
      <path class="wave-band" d="M0,48 C200,3 400,28 585,160 C730,265 870,250 1000,222 L1000,570 L795,570 C720,492 620,458 460,454 C300,452 150,462 0,414 Z"/>
      <path class="wave-field" d="M0,66 C200,22 380,60 560,198 C700,308 850,322 1000,312 L1000,570 L862,570 C760,470 650,422 480,426 C300,430 150,440 0,400 Z"/>
    </svg>

    <div class="owners">
      <div class="owners-names">Mai Torres &amp; Bo Rinaldi</div>
      <div class="owners-role">Owner</div>
    </div>

    <div class="brand">
      <span class="brand-dot"></span>
      <span class="brand-name">Velvet Harbor</span>
    </div>

    <ul class="contact-list">
      <li class="contact-item">
        <svg class="contact-icon" viewBox="0 0 30 30" aria-hidden="true">
          <circle cx="15" cy="15" r="13" fill="none" stroke="#1c1c1c" stroke-width="2"/>
          <circle cx="15" cy="15" r="10" fill="#3a3a3a"/>
          <rect x="9" y="11" width="12" height="8.5" fill="#fff"/>
          <path d="M9 11 L15 16 L21 11" fill="none" stroke="#3a3a3a" stroke-width="1.2"/>
        </svg>
        <span class="contact-text">shop@velvetharbor-example.com</span>
      </li>
      <li class="contact-item">
        <svg class="contact-icon" viewBox="0 0 30 30" aria-hidden="true">
          <circle cx="15" cy="15" r="13" fill="none" stroke="#1c1c1c" stroke-width="2"/>
          <circle cx="15" cy="15" r="10" fill="#3a3a3a"/>
          <g fill="none" stroke="#fff" stroke-width="1.1">
            <circle cx="15" cy="15" r="6.5"/>
            <ellipse cx="15" cy="15" rx="3" ry="6.5"/>
            <line x1="8.5" y1="15" x2="21.5" y2="15"/>
            <line x1="9.5" y1="11.5" x2="20.5" y2="11.5"/>
            <line x1="9.5" y1="18.5" x2="20.5" y2="18.5"/>
          </g>
        </svg>
        <span class="contact-text">www.velvetharbor-example.com</span>
      </li>
    </ul>
  </section>
</main>
</body>
</html>
```